Conservative, Modern and Sharp Builder Business card

Hi there,
We would like to update our existing business card.
I have attached photos of existing business card, logo and van sign.

I would like the business card to also list what we do :
Renovation • New Build • Alteration
Extension • Bathroom • Maintenance.(Seperated by dots)

Contact number : 021 0483 0752
(With that exact spacing)

Ideally when people looking from about 2-3 metres, they know that it is a builder’s business card

Open to suggestions on fonts, layout, style of business card

PLEASE ONLY SUBMIT YOUR BEST OR MAX 3 DESIGNS FOR EACH DESIGNER

Thanks

Industry/Entity Type

Construction. Renovation

Contact Information for Business Card

Details should be the same as the existing card. And addition of what we do.

Requirements
Should not have
• The new business card must not have the same layout as our existing one. Thanks

```html
<!DOCTYPE html>
<html lang="en">
<head>
<meta charset="utf-8">
<title>KeelBuild – Business Card</title>
<link rel="stylesheet" href="https://fonts.googleapis.com/css2?family=Jost:wght@500;600&family=Montserrat:wght@500;600&display=swap">
<style>
  :root {
    --page: #ffffff;
    --card: #ededed;
    --ink: #2f2a2a;
    --ink-dark: #121212;
    --shadow: rgba(0,0,0,0.22);
  }
  html, body {
    margin: 0;
    padding: 0;
    width: 1200px;
    height: 1057px;
    overflow: hidden;
    background: var(--page);
  }
  .canvas { position: relative; width: 1200px; height: 1057px; }
  .card {
    position: absolute;
    left: 334px;
    width: 534px;
    height: 305px;
    background: var(--card);
    box-shadow: 7px 7px 9px var(--shadow);
    overflow: hidden;
  }
  .card--front { top: 199px; }
  .card--back { top: 556px; }

  /* Front */
  .brand-name {
    position: absolute;
    left: 0; width: 224px;
    top: 158px;
    text-align: center;
    font-family: "Jost", sans-serif;
    font-weight: 600;
    font-size: 31px;
    color: var(--ink-dark);
    letter-spacing: -0.3px;
  }
  .divider {
    position: absolute;
    left: 223px; top: 66px;
    width: 2px; height: 172px;
    background: var(--ink);
  }
  .person {
    position: absolute;
    left: 252px; width: 254px;
    top: 46px;
    text-align: center;
  }
  .person__name {
    margin: 0;
    font-family: "Jost", sans-serif;
    font-weight: 500;
    font-size: 35px;
    line-height: 40px;
    color: var(--ink);
  }
  .person__role {
    margin: 6px 0 0;
    font-family: "Montserrat", sans-serif;
    font-weight: 500;
    font-size: 11px;
    letter-spacing: 3.2px;
    color: var(--ink);
  }
  .contacts {
    position: absolute;
    left: 267px; top: 139px;
    margin: 0; padding: 0;
    list-style: none;
  }
  .contacts li {
    display: flex;
    align-items: center;
    height: 20px;
    margin-bottom: 10.5px;
    font-family: "Montserrat", sans-serif;
    font-weight: 500;
    font-size: 13px;
    color: var(--ink-dark);
  }
  .contacts svg { width: 20px; height: 20px; margin-right: 7px; flex: none; }

  /* Back */
  .back-title {
    position: absolute;
    left: 0; right: 0; top: 41px;
    text-align: center;
    font-family: "Montserrat", sans-serif;
    font-weight: 500;
    font-size: 13px;
    letter-spacing: 16px;
    padding-left: 16px;
    color: var(--ink-dark);
  }
  .services {
    position: absolute;
    top: 93px;
    margin: 0; padding: 0;
    list-style: none;
    font-family: "Jost", sans-serif;
    font-weight: 500;
    font-size: 30px;
    line-height: 34px;
    color: var(--ink);
  }
  .services--left { left: 92px; }
  .services--right { left: 312px; }
  .services li { position: relative; }
  .services li::before {
    content: "";
    position: absolute;
    left: -38px; top: 11px;
    width: 9px; height: 9px;
    border-radius: 50%;
    background: var(--ink-dark);
  }
  .rule { position: absolute; top: 244px; }
  .rule--left { left: 36px; }
  .rule--right { left: 318px; }
  .back-mark {
    position: absolute;
    left: 215px; width: 103px;
    top: 236px;
    text-align: center;
    font-family: "Jost", sans-serif;
    font-weight: 600;
    font-size: 15px;
    color: var(--ink-dark);
  }
</style>
</head>
<body>
<main class="canvas">
  <section class="card card--front">
    <div class="brand-name">KeelBuild</div>
    <div class="divider"></div>
    <div class="person">
      <h1 class="person__name">Daren Holloway</h1>
      <p class="person__role">RESIDENTIAL BUILDER</p>
    </div>
    <ul class="contacts">
      <li>
        <svg viewBox="0 0 20 20"><circle cx="10" cy="10" r="9" fill="none" stroke="#121212" stroke-width="1.2"/><path d="M7.2 5.5l1.6 2.3-1 1c.6 1.3 1.6 2.3 2.9 2.9l1-1 2.3 1.6-.9 1.6c-3.4-.2-6.5-3.3-6.7-6.7z" fill="#121212"/></svg>
        021 0483 0752
      </li>
      <li>
        <svg viewBox="0 0 20 20"><circle cx="10" cy="10" r="9" fill="none" stroke="#121212" stroke-width="1.2"/><rect x="6" y="7.2" width="8" height="5.6" fill="#121212"/><path d="M6 7.2l4 3 4-3" fill="none" stroke="#ededed" stroke-width="0.9"/></svg>
        hello@KeelBuild.nz
      </li>
      <li>
        <svg viewBox="0 0 20 20"><circle cx="10" cy="10" r="9" fill="none" stroke="#121212" stroke-width="1.2"/><g fill="none" stroke="#121212" stroke-width="0.9"><circle cx="10" cy="10" r="5.5"/><ellipse cx="10" cy="10" rx="2.4" ry="5.5"/><path d="M4.5 10h11M5.3 7.3h9.4M5.3 12.7h9.4"/></g></svg>
        www.KeelBuild.nz
      </li>
      <li>
        <svg viewBox="0 0 20 20"><circle cx="10" cy="10" r="9" fill="none" stroke="#121212" stroke-width="1.2"/><circle cx="10" cy="10" r="3.2" fill="#121212"/></svg>
        KeelBuild.nz
      </li>
    </ul>
  </section>

  <section class="card card--back">
    <div class="back-title">KEEL BUILD</div>
    <ul class="services services--left">
      <li>Renovation</li>
      <li>New Build</li>
      <li>Alteration</li>
    </ul>
    <ul class="services services--right">
      <li>Extension</li>
      <li>Bathroom</li>
      <li>Maintenance</li>
    </ul>
    <svg class="rule rule--left" width="180" height="6" viewBox="0 0 180 6"><polygon points="0,3 180,0.5 180,5.5" fill="#2f2a2a"/></svg>
    <div class="back-mark">KeelBuild</div>
    <svg class="rule rule--right" width="180" height="6" viewBox="0 0 180 6"><polygon points="0,0.5 180,3 0,5.5" fill="#2f2a2a"/></svg>
  </section>
</main>
</body>
</html>
```